Software Product Website Design

We have a software product which we have just renamed from Milestone Linked Tracking (MLT) to Brolvane. The web site is for www.brolvane-demo.com and needs to contain certain information related to our software product in accordance with the information contained in the previous product brochure (see attached). The logo file is also attached but the designer is free to propose alternative logo colours. The theme for the website must be based on the selected logo colours..
Target Market(s)
Project Management, Engineering, Construction etc companies involved with projects in all industries world-wide
Industry/Entity Type
Software
Coding
Coded - Design and coding required
Number of Pages Required
1 page
Font styles to use
Requirements
Must have
- Professional but exciting theme. The contents of the attached brochure should be included.

```html
<!DOCTYPE html>
<html lang="en">
<head>
<meta charset="utf-8">
<title>Brolvane – Professional Software Development</title>
<link rel="stylesheet" href="https://fonts.googleapis.com/css2?family=Roboto:wght@300;400;500;700&family=Roboto+Condensed:wght@300;400;700&display=swap">
<style>
:root{
  --blue:#2b4ea6;
  --blue-dark:#1f3d8a;
  --pink:#e0155f;
  --red:#c4123a;
  --ink:#333;
  --muted:#888;
  --line:#e2e2e2;
  --foot:#f1f1f1;
  --foot-bottom:#e4e4e4;
}
*{box-sizing:border-box;margin:0;padding:0}
html,body{width:1200px;height:3032px;overflow:hidden}
body{font-family:"Roboto",Arial,sans-serif;color:var(--ink);background:#fff;font-size:14px}
h1,h2,h3,h4{font-family:"Roboto Condensed","Arial Narrow",sans-serif;font-weight:400}

/* header */
.site-header{height:100px;display:flex;align-items:center;justify-content:space-between;padding:0 100px}
.brand{display:flex;align-items:center;gap:10px;font-size:22px;font-weight:500;color:var(--ink)}
.brand-mark{width:26px;height:26px;background:var(--red);border-radius:4px}
.main-nav{display:flex;gap:28px;font-size:13px}
.main-nav a{color:#444;text-decoration:none}

/* hero */
.hero{position:relative;height:520px;background:linear-gradient(160deg,#e9ebee 0%,#bfc3c9 45%,#7d8189 100%)}
.hero h1{position:absolute;left:100px;top:210px;color:#fff;font-size:58px;line-height:1.05;letter-spacing:1px;text-transform:uppercase;font-weight:400}
.hero-arrow{position:absolute;top:355px;width:34px;height:70px;background:#333;display:flex;align-items:center;justify-content:center}
.hero-arrow.prev{left:0}.hero-arrow.next{right:0}
.hero-rule{height:10px;background:linear-gradient(to bottom,var(--red) 0 50%,var(--blue) 50% 100%)}

/* welcome */
.welcome{height:670px;padding-top:120px;text-align:center}
.section-title{font-size:38px;color:#333;text-transform:uppercase;letter-spacing:1px}
.title-rule{width:80px;height:3px;background:var(--blue);margin:18px auto 24px}
.intro{width:1000px;margin:0 auto;font-size:11px;color:var(--muted);line-height:1.7}
.features{display:flex;gap:29px;padding:0 100px;margin-top:70px}
.feature{width:228px;height:268px;position:relative}
.feature-box{height:240px;border:1px solid var(--line);display:flex;flex-direction:column;align-items:center;justify-content:center;gap:22px;padding:0 20px}
.feature-box h3{font-family:"Roboto",sans-serif;font-size:15px;color:#333}
.feature-bar{position:absolute;bottom:0;left:0;width:100%;height:14px;background:var(--blue)}
.feature.active .feature-box{background:var(--blue);border-color:var(--blue);color:#fff;gap:12px}
.feature.active h3{color:#fff;font-weight:700;font-size:14px}
.feature.active p{font-size:10px;line-height:1.7}

/* products */
.products{height:460px;background:linear-gradient(180deg,var(--pink),var(--red));padding-top:50px;text-align:center;color:#fff}
.products .section-title{color:#fff;font-size:36px}
.products .title-rule{background:#fff;margin:14px auto 40px}
.product-row{display:flex;gap:60px;padding:0 100px}
.product{width:225px}
.product-thumb{height:180px;background:#fff;display:flex;align-items:center;justify-content:center;font-size:34px;font-weight:700}
.product-thumb.photo{background:linear-gradient(135deg,#7a6f73,#a89fa3)}
.product-meta{display:flex;justify-content:space-between;font-size:17px;margin-top:18px;text-transform:uppercase}
.carousel-nav{display:flex;gap:10px;justify-content:center;margin-top:56px}
.carousel-nav span{width:34px;height:34px;border-radius:50%;background:var(--blue);display:flex;align-items:center;justify-content:center}

/* faq + testimonials */
.info{height:440px;display:flex;gap:60px;padding:80px 100px 0;border-bottom:1px solid var(--line)}
.info h2{font-size:20px;text-transform:uppercase;margin-bottom:6px}
.info .rule{width:40px;height:3px;background:var(--blue);margin-bottom:30px}
.faq{width:480px}
.faq-list{border:1px solid var(--line);padding:6px 10px}
.faq-item{display:flex;justify-content:space-between;font-size:12px;padding:11px 4px;border-bottom:1px solid var(--line);color:#555}
.faq-item:last-child{border-bottom:0}
.testimonials{width:460px}
.quote{border:1px solid var(--line);border-left:4px solid var(--blue);padding:14px 18px;font-size:12px;color:#666;line-height:1.7;font-style:italic;display:flex;gap:12px}
.quote b{font-size:42px;color:#bbb;font-style:normal;line-height:.8}
.reviewer{text-align:center;margin-top:36px}
.avatar{width:64px;height:64px;border-radius:50%;background:linear-gradient(#c9ccd2,#8b8f96);margin:0 auto 10px}
.reviewer strong{display:block;font-size:13px}
.reviewer small{color:var(--muted);font-size:11px}

/* clients */
.clients{height:350px;padding-top:120px;text-align:center}
.clients h2{font-size:24px;text-transform:uppercase}
.client-row{display:flex;justify-content:space-between;padding:0 130px;margin-top:60px}
.client{display:flex;align-items:center;gap:8px;font-size:18px;font-weight:700;color:var(--blue)}
.client i{width:22px;height:22px;background:var(--red);border-radius:50%}

/* cta */
.cta{height:100px;background:var(--blue);color:#fff;display:flex;align-items:center;justify-content:center;font-family:"Roboto Condensed",sans-serif;font-size:30px;font-weight:700}
.cta a{color:#fff;margin-left:10px}

/* footer */
.site-footer{height:332px;background:var(--foot);display:flex;gap:40px;padding:40px 100px 0}
.footer-col{width:220px;font-size:11px;color:#666;line-height:1.7}
.footer-col h4{font-family:"Roboto",sans-serif;font-size:12px;font-weight:700;color:#333;text-transform:uppercase;margin-bottom:12px}
.footer-col p{margin-bottom:12px}
.footer-col ul{list-style:none}
.socials{display:flex;gap:8px;margin-top:10px}
.socials span{width:20px;height:20px;border-radius:50%;background:#aaa}
.footer-bottom{height:50px;background:var(--foot-bottom);display:flex;align-items:center;justify-content:space-between;padding:0 100px;font-size:11px;color:#777}
.to-top{width:26px;height:26px;border-radius:50%;background:#999}
</style>
</head>
<body>

<header class="site-header">
  <div class="brand"><span class="brand-mark"></span>brolvane</div>
  <nav class="main-nav">
    <a href="#">Home</a><a href="#">About</a><a href="#">Get a Business Name</a><a href="#">Testimonials</a><a href="#">Contact</a>
  </nav>
</header>

<section class="hero" role="img" aria-label="Photo of project reports and charts on a desk with a pen">
  <h1>Professional<br>Software Development</h1>
  <span class="hero-arrow prev"><svg width="12" height="20"><path d="M10 2 2 10l8 8" stroke="#fff" stroke-width="2" fill="none"/></svg></span>
  <span class="hero-arrow next"><svg width="12" height="20"><path d="M2 2l8 8-8 8" stroke="#fff" stroke-width="2" fill="none"/></svg></span>
</section>
<div class="hero-rule"></div>

<section class="welcome">
  <h2 class="section-title">Welcome to Brolvane</h2>
  <div class="title-rule"></div>
  <p class="intro">Brolvane links every project milestone to measurable progress so teams see status, cost and schedule in one place. Built for project management, engineering and construction companies working across all industries world-wide, it replaces manual reporting with clear, milestone linked tracking that owners and contractors can trust every day.</p>
  <div class="features">
    <div class="feature">
      <div class="feature-box">
        <svg width="40" height="36" viewBox="0 0 40 36"><path d="M20 33S3 22 3 11a8 8 0 0 1 17-3 8 8 0 0 1 17 3c0 11-17 22-17 22z" fill="none" stroke="#333" stroke-width="2.5"/></svg>
        <h3>Creative Design</h3>
      </div><span class="feature-bar"></span>
    </div>
    <div class="feature active">
      <div class="feature-box">
        <h3>Magical Animations</h3>
        <p>Smooth progress views show each milestone moving from plan to done, with clear status at every step of the project.</p>
      </div><span class="feature-bar"></span>
    </div>
    <div class="feature">
      <div class="feature-box">
        <svg width="44" height="30" viewBox="0 0 44 30"><path d="M12 5 3 15l9 10M32 5l9 10-9 10M25 2l-6 26" fill="none" stroke="#333" stroke-width="2.5"/></svg>
        <h3>Clean Code</h3>
      </div><span class="feature-bar"></span>
    </div>
    <div class="feature">
      <div class="feature-box">
        <svg width="40" height="36" viewBox="0 0 40 36"><path d="M37 3 3 17l13 4 4 12 17-30zM16 21 37 3" fill="none" stroke="#333" stroke-width="2.5"/></svg>
        <h3>24/7 Support</h3>
      </div><span class="feature-bar"></span>
    </div>
  </div>
</section>

<section class="products">
  <h2 class="section-title">Our Product</h2>
  <div class="title-rule"></div>
  <div class="product-row">
    <div class="product"><div class="product-thumb photo" role="img" aria-label="Photo of office icons on a desk"></div><div class="product-meta"><span>Product</span><span>$ 1365</span></div></div>
    <div class="product"><div class="product-thumb" style="color:#e8a21a">Varnelle</div><div class="product-meta"><span>Product</span><span>$ 1365</span></div></div>
    <div class="product"><div class="product-thumb" style="color:#1aa37a">Quorbit</div><div class="product-meta"><span>Product</span><span>$ 1365</span></div></div>
    <div class="product"><div class="product-thumb" style="color:#7a2a8c">Tessaly</div><div class="product-meta"><span>Product</span><span>$ 1365</span></div></div>
  </div>
  <div class="carousel-nav">
    <span><svg width="10" height="14"><path d="M8 2 2 7l6 5" stroke="#fff" stroke-width="2" fill="none"/></svg></span>
    <span><svg width="10" height="14"><path d="M2 2l6 5-6 5" stroke="#fff" stroke-width="2" fill="none"/></svg></span>
  </div>
</section>

<section class="info">
  <div class="faq">
    <h2>FAQs</h2><div class="rule"></div>
    <div class="faq-list">
      <div class="faq-item"><span>How does Brolvane link milestones to cost?</span><span>+</span></div>
      <div class="faq-item"><span>Can teams share reports with the client?</span><span>+</span></div>
      <div class="faq-item"><span>Which industries use milestone tracking?</span><span>+</span></div>
      <div class="faq-item"><span>Is training included with the licence?</span><span>+</span></div>
      <div class="faq-item"><span>How is project data kept secure?</span><span>+</span></div>
    </div>
  </div>
  <div class="testimonials">
    <h2>Testimonials</h2><div class="rule"></div>
    <div class="quote"><b>“</b><p>Brolvane gave our engineering team one clear view of progress. Milestone reports that took days now take minutes, and our clients finally see the same numbers we do.</p></div>
    <div class="reviewer">
      <div class="avatar" role="img" aria-label="Portrait of the reviewer"></div>
      <strong>Marla Venn</strong>
      <small>Director, Construction</small>
    </div>
  </div>
</section>

<section class="clients">
  <h2>Our Best Clients</h2>
  <div class="client-row">
    <span class="client"><i></i>Oskaro</span>
    <span class="client"><i></i>Halcyra</span>
    <span class="client"><i></i>Halcyra</span>
    <span class="client"><i></i>Oskaro</span>
    <span class="client"><i></i>Oskaro</span>
    <span class="client"><i></i>Dunmere</span>
  </div>
</section>

<section class="cta">Get A Free Quote / Need a Help ? <a href="#">Contact Us</a></section>

<footer>
  <div class="site-footer">
    <div class="footer-col">
      <h4>About Us</h4>
      <p>Brolvane helps project teams track milestones, cost and progress in one simple shared view.</p>
      <p>Office: 14 Harbour Lane, Suite 3, North Quay<br>Call Us: +00 000 000 0000<br>www.brolvane-demo.com</p>
    </div>
    <div class="footer-col">
      <h4>Business</h4>
      <ul><li>Milestone Linked Tracking</li><li>Progress Reports</li><li>Cost Control</li><li>FAQ</li><li>Support</li><li>Latest Blog</li></ul>
      <h4 style="margin-top:16px">My Account</h4>
      <ul><li>My account</li><li>Order History</li><li>Shopping Cart</li></ul>
    </div>
    <div class="footer-col">
      <h4>Latest News</h4>
      <p>New reporting dashboard released for all project teams this month.</p>
      <p>Brolvane now supports multi site construction programmes.</p>
      <p>Webinar: linking milestones to payment schedules.</p>
    </div>
    <div class="footer-col">
      <h4>Newsletter Signup</h4>
      <p>Subscribe to our newsletter to get product news, tips and updates.</p>
      <p><strong>Total downloads: 12530</strong></p>
      <p><strong>Happy users: 7851</strong></p>
      <div class="socials"><span></span><span></span><span></span><span></span><span></span></div>
    </div>
  </div>
  <div class="footer-bottom"><span>© 2024 Brolvane. All rights reserved. Terms of Use | Privacy Policy</span><span class="to-top"></span></div>
</footer>

</body>
</html>
```